Derek Hollins Business card

Hey there, I’m hoping to have a business card designed. I’m in Real estate and just switched to a new Brokerage called: The Property Quarter

The back could just be the company name maybe or whatever looks good!

I’ve attached some logos of our company and some cards my buddy had done up.

On the card:
Derek Hollins
derekhollins@mailbox-demo.com
587-214-6093
derekhollins-demo.ca

Target Market(s)

Home buyers and sellers

Industry/Entity Type

Real Estate

Contact Information for Business Card

just looking for a cool and modern design with my picture on it. I like the idea of Black and red being used.

Requirements
Must have
• all the details provided. I'm open to anything. Just want a professional looking card.

```html
<!DOCTYPE html>
<html lang="en">
<head>
<meta charset="utf-8">
<title>Derek Hollins – Business Card</title>
<link href="https://fonts.googleapis.com/css2?family=Roboto:wght@400;500;700;900&display=swap" rel="stylesheet">
<style>
  :root {
    --page: #2b2b2d;
    --card: #222026;
    --card-deep: #18171b;
    --accent: #d51f35;
    --ink: #ffffff;
    --shade: #2e2c33;
  }
  * { box-sizing: border-box; margin: 0; padding: 0; }
  html, body { width: 1200px; height: 852px; overflow: hidden; }
  body {
    background: var(--page);
    font-family: "Roboto", Arial, sans-serif;
    position: relative;
  }
  .card {
    position: absolute;
    width: 520px;
    height: 310px;
    background: var(--card);
    border: 3px solid var(--accent);
    border-radius: 24px;
    overflow: hidden;
    box-shadow: 0 18px 40px rgba(0,0,0,.45);
  }
  .card-back { left: 120px; top: 90px; }
  .card-front { left: 560px; top: 450px; }

  .back-pattern {
    position: absolute; inset: 0;
    background: linear-gradient(135deg, #232127 0%, #1b1a1f 50%, #232127 100%);
  }
  .back-brand {
    position: absolute;
    right: 56px; bottom: 92px;
    display: flex; align-items: center; gap: 8px;
    color: var(--ink);
    font-weight: 900;
    font-size: 22px;
    letter-spacing: .5px;
    text-transform: uppercase;
  }
  .back-brand .mark {
    width: 12px; height: 12px; background: var(--accent);
  }

  .initial {
    position: absolute;
    right: -30px; top: -90px;
    font-weight: 900;
    font-size: 460px;
    line-height: 1;
    color: var(--card-deep);
    text-shadow: -2px -2px 0 var(--shade);
  }
  .portrait {
    position: absolute;
    left: 60px; top: 26px;
    width: 140px; height: 140px;
    border-radius: 50%;
    border: 3px solid var(--accent);
    padding: 6px;
    background: var(--card);
  }
  .portrait-fill {
    width: 100%; height: 100%;
    border-radius: 50%;
    background: radial-gradient(circle at 50% 40%, #f4f1ee 0%, #d9d3cf 55%, #3a3a42 100%);
  }
  .accent-tab {
    position: absolute;
    left: 0; top: 190px;
    width: 24px; height: 30px;
    background: var(--accent);
  }
  .details {
    position: absolute;
    left: 92px; top: 180px;
  }
  .name {
    color: var(--accent);
    font-weight: 500;
    font-size: 26px;
    margin-bottom: 8px;
  }
  .contact { list-style: none; }
  .contact li {
    display: flex; align-items: center; gap: 8px;
    color: var(--ink);
    font-size: 15px;
    line-height: 22px;
  }
  .contact svg { width: 13px; height: 13px; flex: none; }
</style>
</head>
<body>

<section class="card card-back">
  <div class="back-pattern" role="img" aria-label="Repeating embossed brokerage name pattern in dark tones"></div>
  <div class="back-brand"><span class="mark"></span>The Property Quarter</div>
</section>

<section class="card card-front">
  <div class="initial" aria-hidden="true">D</div>
  <div class="portrait">
    <div class="portrait-fill" role="img" aria-label="Portrait photo of Derek Hollins"></div>
  </div>
  <div class="accent-tab"></div>
  <div class="details">
    <h1 class="name">Derek Hollins</h1>
    <ul class="contact">
      <li>
        <svg viewBox="0 0 16 16"><path fill="#d51f35" d="M3 1h3l1.5 4-2 1.3a9 9 0 0 0 4.2 4.2L11 8.5l4 1.5v3a2 2 0 0 1-2 2A12 12 0 0 1 1 3a2 2 0 0 1 2-2z"/></svg>
        587-214-6093
      </li>
      <li>
        <svg viewBox="0 0 16 16"><rect x="1" y="3" width="14" height="10" rx="1" fill="#d51f35"/><path d="M1.5 4l6.5 5 6.5-5" stroke="#222026" stroke-width="1.4" fill="none"/></svg>
        derekhollins@mailbox-demo.com
      </li>
      <li>
        <svg viewBox="0 0 16 16"><circle cx="8" cy="8" r="7" fill="#d51f35"/><path d="M1 8h14M8 1c-3 3.5-3 10.5 0 14M8 1c3 3.5 3 10.5 0 14" stroke="#222026" stroke-width="1.1" fill="none"/></svg>
        derekhollins-demo.ca
      </li>
    </ul>
  </div>
</section>

</body>
</html>
```